Tequila Bottle Labels

We are a construction company that bottled our own tequila and would like a unique label for it! We already have our own company logo (linked below) and we want that logo somewhere on the bottle as well- it can be big or small. It was brewed & bottled in Southern California. Ideally it would have the year "2020," "Single Estate," & "100% Agave Azul" somewhere on the label.

Tequila / RMT / 2020

```html
<!DOCTYPE html>
<html lang="en">
<head>
<meta charset="UTF-8">
<title>RMT 2020 Tequila Label</title>
<link rel="stylesheet" href="https://fonts.googleapis.com/css2?family=Cinzel:wght@400;700&family=Playfair+Display:wght@700&family=Arimo:wght@400;700&display=swap">
<style>
  :root {
    --label-cream: #f3f0cf;
    --brand-navy: #173a6e;
    --agave-green: #8dc63f;
    --olive-green: #4f6d1f;
    --flourish-tone: #8a97a8;
  }
  * { margin: 0; padding: 0; box-sizing: border-box; }
  html, body {
    width: 1199px;
    height: 1200px;
    overflow: hidden;
    background: var(--label-cream);
  }
  .label {
    position: relative;
    width: 1199px;
    height: 1200px;
    color: var(--brand-navy);
  }
  .label > * {
    position: absolute;
    left: 0;
    width: 100%;
    text-align: center;
  }
  .brand-name {
    top: 520px;
    font-family: "Cinzel", serif;
    font-weight: 700;
    font-size: 116px;
    line-height: 1;
    letter-spacing: 4px;
    color: var(--brand-navy);
  }
  .vintage-year {
    top: 652px;
    font-family: "Playfair Display", serif;
    font-weight: 700;
    font-size: 52px;
    line-height: 1;
    letter-spacing: 3px;
    color: var(--brand-navy);
  }
  .vintage-year .accent { color: var(--agave-green); }
  .product-type {
    top: 748px;
    font-family: "Cinzel", serif;
    font-weight: 400;
    font-size: 50px;
    line-height: 1;
    letter-spacing: 3px;
    color: var(--brand-navy);
  }
  .flourish {
    top: 806px;
    left: 549px;
    width: 100px;
    height: 28px;
    border-radius: 14px;
    background: linear-gradient(90deg, transparent, var(--flourish-tone) 25%, var(--flourish-tone) 75%, transparent);
    opacity: 0.3;
  }
  .agave-note {
    top: 850px;
    font-family: "Cinzel", serif;
    font-weight: 400;
    font-size: 19px;
    line-height: 1.1;
    color: var(--brand-navy);
  }
  .strength {
    top: 930px;
    font-family: "Arimo", sans-serif;
    font-size: 18px;
    color: var(--olive-green);
  }
  .volume {
    top: 996px;
    font-family: "Arimo", sans-serif;
    font-weight: 700;
    font-size: 20px;
    color: var(--brand-navy);
  }
</style>
</head>
<body>
  <main class="label">
    <div class="brand-name">RMT</div>
    <div class="vintage-year">20<span class="accent">20</span></div>
    <h1 class="product-type">Tequila</h1>
    <span class="flourish" role="img" aria-label="Decorative calligraphic flourish divider"></span>
    <p class="agave-note">100%<br>Agave Azul</p>
    <p class="strength">40% alcohol</p>
    <p class="volume">750ml</p>
  </main>
</body>
</html>
```